Business Card Design Project

for a second hand vintage clothing store. shop name is The Velvet Loft

Cards to be double sided

The name on the card is Marianne Trelford

Information to put on card:

The Velvet Loft
Marianne Trelford (no job title)
84/227 Quayle St, Pyrmont, Sydney, NSW, 2009.
Mobile: 0412 975 206
Email: thevelvetloft@mailbox-example.com.au
Web: www.thevelvetloft-example.com.au

Target Market(s)

Women looking at vintage clothing

Industry/Entity Type

Clothing

```html
<!DOCTYPE html>
<html lang="en">
<head>
<meta charset="utf-8">
<title>The Velvet Loft – Business Card</title>
<link rel="stylesheet" href="https://fonts.googleapis.com/css2?family=Tinos:wght@400&display=swap">
<style>
  :root {
    --backdrop: #97a2a8;
    --plum: #44112f;
    --plum-ink: #4a1640;
    --cream-gold: #ebe08a;
    --card-white: #ffffff;
  }
  * { margin: 0; padding: 0; box-sizing: border-box; }
  html, body {
    width: 1200px;
    height: 900px;
    overflow: hidden;
    background: var(--backdrop);
    font-family: "Tinos", "Times New Roman", serif;
  }
  .canvas {
    position: relative;
    width: 1200px;
    height: 900px;
  }
  .card {
    position: absolute;
    left: 335px;
    width: 538px;
    height: 370px;
  }
  .card--front {
    top: 60px;
    background: var(--plum);
  }
  .card--back {
    top: 460px;
    background: var(--card-white);
  }
  .brand-name {
    position: absolute;
    white-space: nowrap;
    font-weight: 400;
    line-height: 1;
  }
  .card--front .brand-name {
    left: 0;
    right: 0;
    top: 165px;
    text-align: center;
    font-size: 58px;
    color: var(--cream-gold);
  }
  .card--back .brand-name {
    right: 42px;
    top: 280px;
    font-size: 34px;
    color: var(--plum-ink);
  }
  .contact {
    position: absolute;
    left: 47px;
    top: 42px;
    list-style: none;
    color: var(--plum-ink);
    font-size: 21px;
    line-height: 27px;
  }
</style>
</head>
<body>
  <main class="canvas">
    <section class="card card--front" aria-label="Card front">
      <p class="brand-name">The Velvet Loft</p>
    </section>

    <section class="card card--back" aria-label="Card back">
      <ul class="contact">
        <li class="contact__name">Marianne Trelford</li>
        <li class="contact__address">84/227 Quayle St, Pyrmont, Sydney, NSW, 2009</li>
        <li class="contact__mobile">Mob: 0412 975 206</li>
        <li class="contact__email">thevelvetloft@mailbox-example.com.au</li>
        <li class="contact__web">www.thevelvetloft-example.com.au</li>
      </ul>
      <p class="brand-name">The Velvet Loft</p>
    </section>
  </main>
</body>
</html>
```